Executive Taxi firm with Chauffeur service Website

I have my domain name registered and I have started to work on my site but I am struggling. I am just about to get a logo for the company and need a web site that clearly represents the fact we are an executive/luxury brand in private hire vehicles. We offer airport transfers, train station transfers, seaport transfers, holiday transfers and business to business pick up and drop off.

Target Market(s)

Corporate people, holidaymakers looking for a luxury start their holiday. VIPs' and celebrities.

Number of Pages Required

5+ page

Font styles to use
Serif
Sans Serif
Decorative
Script

Colors

Designer to choose colors to be used in the design.

Requirements
Must have
• Home Page, Services, About Us, VIP and Contact us
• Please see www.brovencars.co.uk I have started it but not happy with it at all.
Nice to have
• Booking form or enquiry form.

```html
<!DOCTYPE html>
<html lang="en">
<head>
<meta charset="utf-8">
<title>Broven Cars – Executive Chauffeur Service</title>
<link rel="stylesheet" href="https://fonts.googleapis.com/css2?family=Open+Sans:ital,wdth,wght@0,75..100,300..800&display=swap">
<style>
:root{
  --gold:#f0c400;
  --ink:#222;
  --tile:#2f2f2f;
  --booking:#2a2a2a;
  --footer:#3a3a3a;
  --mist:#eeeeee;
  --field:#e6e6e6;
  --muted:#bdbdbd;
  --white:#fff;
}
*{box-sizing:border-box;margin:0;padding:0}
html,body{width:1200px;height:3152px;overflow:hidden}
body{font-family:"Open Sans",Arial,sans-serif;color:var(--ink);background:var(--white);position:relative}
.cond{font-stretch:75%;font-weight:700}
section,header,footer{position:absolute;left:0;width:1200px}

/* hero */
.hero{top:0;height:614px;background:linear-gradient(160deg,#6d7480 0%,#4a4f57 45%,#2c2e33 100%)}
.hero-photo{position:absolute;inset:0;background:linear-gradient(180deg,rgba(200,205,212,.35) 0%,rgba(60,60,64,.2) 55%,rgba(20,20,22,.55) 100%)}
.brand{position:absolute;left:143px;top:20px;display:flex;align-items:center;gap:14px}
.brand-dot{width:58px;height:58px;border-radius:50%;background:var(--gold)}
.brand-name{font-family:"Open Sans",Arial,sans-serif;font-stretch:75%;font-weight:700;font-size:46px;color:var(--white);line-height:1}
.nav{position:absolute;top:38px;right:143px;display:flex;gap:36px;list-style:none}
.nav a{font-family:"Open Sans",Arial,sans-serif;font-stretch:75%;font-weight:700;font-size:16px;color:var(--white);text-decoration:none;text-transform:uppercase}
.nav a.active{color:var(--gold)}
.hero-arrow{position:absolute;top:328px;width:30px;height:30px}
.hero-copy{position:absolute;left:0;right:0;top:418px;text-align:center;color:var(--white)}
.hero-kicker{font-size:19px}
.hero-title{font-size:44px;line-height:1.2;margin-top:6px}
.btn{display:inline-block;background:var(--gold);color:var(--ink);font-family:"Open Sans",Arial,sans-serif;font-stretch:75%;font-weight:700;text-transform:uppercase;text-decoration:none;text-align:center}
.hero .btn{position:absolute;left:544px;top:511px;width:112px;height:38px;line-height:38px;font-size:16px}

/* welcome */
.welcome{top:614px;height:445px}
.welcome h1{position:absolute;left:143px;top:72px;font-size:33px;color:var(--gold);text-transform:uppercase}
.welcome-body{position:absolute;left:143px;top:124px;width:690px;display:flex;flex-direction:column;align-items:flex-start}
.welcome .text{font-size:11.2px;line-height:22px}
.welcome .text p+p{margin-top:20px}
.welcome .btn{margin-top:22px;width:111px;height:38px;line-height:38px;font-size:15px}
.app-visual{position:absolute;left:850px;top:80px;width:214px;height:284px;overflow:hidden;background:radial-gradient(circle at 50% 56%,#111 0 95px,transparent 96px)}

/* services */
.services{top:1059px;height:591px;background:var(--gold)}
.services h2{position:absolute;left:143px;top:74px;font-size:32px;text-transform:uppercase}
.services .intro{position:absolute;left:143px;top:116px;width:296px;font-size:11.2px;line-height:20px}
.tile{position:absolute;width:291px;height:206px;background:var(--tile);color:var(--white);display:flex;flex-direction:column;align-items:center;padding-top:28px;text-align:center}
.tile svg{width:82px;height:82px;stroke:var(--white);fill:none;stroke-width:2.2;stroke-linecap:round;stroke-linejoin:round}
.tile h3{font-size:22px;line-height:26px;text-transform:uppercase;margin-top:14px}

/* reviews */
.reviews{top:1650px;height:334px;text-align:center}
.reviews h2{position:absolute;left:0;right:0;top:74px;font-size:32px;color:var(--gold)}
.reviews blockquote{position:absolute;left:140px;right:140px;top:128px;font-size:21px;line-height:28px}
.reviews cite{position:absolute;left:0;right:0;top:190px;font-style:normal;font-size:18px;color:var(--gold)}
.dots{position:absolute;left:0;right:0;top:238px;display:flex;justify-content:center;gap:12px}
.dots span{width:12px;height:12px;border-radius:50%;background:var(--muted)}
.dots span.on{background:var(--gold)}

/* gallery */
.gallery{top:1984px;height:351px;background:var(--mist)}
.gallery h2{position:absolute;left:0;right:0;top:68px;text-align:center;font-size:32px}
.gallery-photo{position:absolute;top:128px;width:213px;height:143px}
.gallery-arrow{position:absolute;top:184px;width:24px;height:30px}

/* stats */
.stats{top:2335px;height:214px}
.stat{position:absolute;top:70px;width:200px;text-align:center}
.stat strong{display:block;font-size:34px;color:var(--gold);line-height:40px}
.stat span{font-size:16px}

/* booking */
.booking{top:2549px;height:376px;background:var(--booking)}
.booking h2{position:absolute;left:0;right:0;top:70px;text-align:center;font-size:33px;color:var(--gold);text-transform:uppercase}
.field{position:absolute;width:288px;height:40px;background:var(--field);font-size:13.5px;color:#333;padding-left:22px;line-height:40px}
.field svg{position:absolute;right:16px;top:12px;width:16px;height:16px;stroke:#333;fill:none;stroke-width:1.6}
.booking .btn{position:absolute;left:551px;top:254px;width:96px;height:40px;line-height:40px;font-size:17px;border:none}

/* footer */
.site-footer{top:2925px;height:227px;background:var(--footer);color:var(--white)}
.site-footer h4{position:absolute;top:28px;font-size:19px;text-transform:uppercase}
.site-footer h4.title{text-transform:none}
.foot-links{position:absolute;left:143px;top:66px;display:grid;grid-template-columns:60px 60px;row-gap:4px;font-size:10.5px;color:var(--muted);list-style:none}
.contact{position:absolute;left:359px;top:64px;font-size:10.5px;color:var(--muted);list-style:none}
.contact li{display:flex;align-items:center;gap:12px;margin-bottom:6px}
.contact svg{width:11px;height:11px;fill:var(--muted)}
.news-note{position:absolute;left:599px;top:66px;font-size:10.5px;color:var(--muted)}
.news-field{position:absolute;left:599px;top:83px;width:256px;height:34px;background:var(--field);color:#333;font-size:13px;line-height:34px;padding-left:22px}
.news-field svg{position:absolute;right:12px;top:10px;width:18px;height:14px;fill:#444}
.social{position:absolute;left:946px;top:66px;display:flex;gap:12px}
.social span{width:28px;height:28px;border-radius:50%;background:#8a8a8a}
.rule{position:absolute;left:143px;right:143px;top:150px;height:1px;background:#5a5a5a}
.copyright{position:absolute;left:0;right:0;top:181px;text-align:center;font-size:10.5px;color:var(--muted)}
</style>
</head>
<body>

<header class="hero">
  <div class="hero-photo" role="img" aria-label="Chauffeur greeting a businessman beside a private jet and executive car on an airfield"></div>
  <div class="brand"><span class="brand-dot"></span><span class="brand-name">Broven Cars</span></div>
  <ul class="nav">
    <li><a class="active" href="#">Home</a></li>
    <li><a href="#">Services</a></li>
    <li><a href="#">About Us</a></li>
    <li><a href="#">VIP</a></li>
    <li><a href="#">Contact Us</a></li>
  </ul>
  <svg class="hero-arrow" style="left:42px" viewBox="0 0 30 30"><path d="M19 5 9 15l10 10" stroke="#fff" stroke-width="3" fill="none"/></svg>
  <svg class="hero-arrow" style="left:1128px" viewBox="0 0 30 30"><path d="M11 5l10 10-10 10" stroke="#fff" stroke-width="3" fill="none"/></svg>
  <div class="hero-copy">
    <p class="hero-kicker cond">Private Hire, Chauffeur and taxi service</p>
    <h1 class="hero-title cond">Executive Broven Cars</h1>
  </div>
  <a class="btn" href="#">Book Now</a>
</header>

<section class="welcome">
  <h1 class="cond">Welcome to Broven Cars</h1>
  <div class="welcome-body">
    <div class="text">
      <p>We provide airport transfers to and from all major UK airports, seaports, train station transfers and an executive business to business transfer service. Whether you have an individual or group transfer request, our company-owned fleet offers a choice of options to suit your needs, from luxury saloons and SUV's to 9-seat luxury transporters.</p>
      <p>We provide a door-to-door convenience from your home, office or hotel straight to any destination of your choice. Pre-booked or last minute we aim to cover any transport requirement. Allports and train station service: All pickups from arrivals will of been briefed as to your exact pickup point, or your chauffeur will be waiting with a name board. We also track your arrival time, so you can relax safe in the knowledge we will be waiting for you whatever time your journey completes.</p>
    </div>
    <a class="btn" href="#">Learn More</a>
  </div>
  <div class="app-visual" role="img" aria-label="Smartphone showing the booking app map over a black circle"></div>
</section>

<section class="services">
  <h2 class="cond">What we do</h2>
  <p class="intro">Fusce sollicitudin lorem et luctus volutpat. Proin placerat dapibus gravida. In tristique tristique nulla eget hendrerit. Maecenas vel tortor accumsan quam varius imperdiet vel eget elit. Aenean facilisis tincidunt lectus, id dictum nisi luctus eget. Vivamus efficitur ex condi-mentum, malesuada eros eget, feugiat nibh.</p>

  <div class="tile" style="left:454px;top:80px">
    <svg viewBox="0 0 80 80"><path d="M40 8c3 0 4 4 4 9v14l26 14v6L44 43v15l8 6v5l-12-3-12 3v-5l8-6V43L10 51v-6l26-14V17c0-5 1-9 4-9z"/></svg>
    <h3 class="cond">Airport Transfers</h3>
  </div>
  <div class="tile" style="left:763px;top:80px">
    <svg viewBox="0 0 80 80"><rect x="20" y="8" width="40" height="50" rx="8"/><rect x="26" y="16" width="28" height="16"/><circle cx="30" cy="45" r="3"/><circle cx="50" cy="45" r="3"/><path d="M26 58l-8 16M54 58l8 16M22 66h36M20 72h40"/></svg>
    <h3 class="cond">Train Station Transfers</h3>
  </div>
  <div class="tile" style="left:143px;top:305px">
    <svg viewBox="0 0 80 80"><path d="M12 46h58l-8 14H20z"/><path d="M22 46V36h36v10M30 36v-8h20v8M36 28v-8h8v8"/><path d="M6 66c5 0 5-3 10-3s5 3 10 3 5-3 10-3 5 3 10 3 5-3 10-3 5 3 10 3 5-3 10-3"/><path d="M6 73c5 0 5-3 10-3s5 3 10 3 5-3 10-3 5 3 10 3 5-3 10-3 5 3 10 3 5-3 10-3"/></svg>
    <h3 class="cond">Seaport Transfers</h3>
  </div>
  <div class="tile" style="left:454px;top:305px">
    <svg viewBox="0 0 80 80"><rect x="12" y="26" width="26" height="42" rx="3"/><path d="M20 26V10h10v16M18 36v22M25 36v22M32 36v22"/><rect x="42" y="34" width="26" height="34" rx="3"/><path d="M50 34v-8h10v8M48 44v16M55 44v16M62 44v16"/><circle cx="17" cy="72" r="2"/><circle cx="33" cy="72" r="2"/><circle cx="47" cy="72" r="2"/><circle cx="63" cy="72" r="2"/></svg>
    <h3 class="cond">Holiday Transfers</h3>
  </div>
  <div class="tile" style="left:763px;top:305px">
    <svg viewBox="0 0 80 80"><rect x="8" y="22" width="64" height="46" rx="4"/><path d="M30 22v-8h20v8M8 38h64M36 34h8v8h-8z"/></svg>
    <h3 class="cond">Business to Business<br>Pick up and Drop off</h3>
  </div>
</section>

<section class="reviews">
  <h2 class="cond">REVIEWS</h2>
  <blockquote class="cond">“Having used so many different taxi firms over the years these guys really know how to look after you. A reall touch of class to your journey.”</blockquote>
  <cite class="cond">James Carter, MD Redford</cite>
  <div class="dots"><span class="on"></span><span></span><span></span><span></span></div>
</section>

<section class="gallery">
  <h2 class="cond">GALLERY</h2>
  <svg class="gallery-arrow" style="left:52px" viewBox="0 0 24 30"><path d="M17 4 7 15l10 11" stroke="#999" stroke-width="2.5" fill="none"/></svg>
  <div class="gallery-photo" role="img" aria-label="Passenger stepping out of a black executive car" style="left:143px;background:linear-gradient(135deg,#8a8d90,#2e3033 60%,#55585c)"></div>
  <div class="gallery-photo" role="img" aria-label="Chauffeur opening the rear door of a black saloon for a client" style="left:377px;background:linear-gradient(135deg,#6f7a5e,#2b2d30 55%,#777b80)"></div>
  <div class="gallery-photo" role="img" aria-label="Chauffeur holding the car door for a businesswoman" style="left:610px;background:linear-gradient(135deg,#9a9ea3,#26282b 55%,#5d6064)"></div>
  <div class="gallery-photo" role="img" aria-label="Chauffeur standing beside an executive saloon outside an office building" style="left:843px;background:linear-gradient(160deg,#a7adb3,#6e747a 50%,#2a2c2f)"></div>
  <svg class="gallery-arrow" style="left:1124px" viewBox="0 0 24 30"><path d="M7 4l10 11-10 11" stroke="#999" stroke-width="2.5" fill="none"/></svg>
</section>

<section class="stats">
  <div class="stat" style="left:150px"><strong class="cond">36,400</strong><span class="cond">Journeys to date</span></div>
  <div class="stat" style="left:383px"><strong class="cond">2</strong><span class="cond">Locations</span></div>
  <div class="stat" style="left:617px"><strong class="cond">8</strong><span class="cond">Staff</span></div>
  <div class="stat" style="left:850px"><strong class="cond">60+</strong><span class="cond">Years</span></div>
</section>

<section class="booking">
  <h2 class="cond">Book a ride with us</h2>
  <div class="field" style="left:143px;top:128px">First Name</div>
  <div class="field" style="left:456px;top:128px">Last Name</div>
  <div class="field" style="left:767px;top:128px">Email</div>
  <div class="field" style="left:143px;top:191px">Phone</div>
  <div class="field" style="left:456px;top:191px">Date<svg viewBox="0 0 16 16"><rect x="1.5" y="3" width="13" height="11.5"/><path d="M1.5 6.5h13M5 1v4M11 1v4M4 9h2M7 9h2M10 9h2M4 12h2M7 12h2"/></svg></div>
  <div class="field" style="left:767px;top:191px">Time<svg viewBox="0 0 16 16"><circle cx="8" cy="8" r="6.5"/><path d="M8 4v4l3 2"/></svg></div>
  <button class="btn" type="button">Submit</button>
</section>

<footer class="site-footer">
  <h4 class="title cond" style="left:143px">Menu</h4>
  <ul class="foot-links">
    <li>Home</li><li>VIP</li><li>Services</li><li>Contact us</li><li>About Us</li>
  </ul>
  <h4 class="title cond" style="left:359px">Contact Info</h4>
  <ul class="contact">
    <li><svg viewBox="0 0 12 12"><path d="M2.5 1l2 2.5-1.2 1.3a7 7 0 0 0 3.9 3.9L8.5 7.5 11 9.5 9.8 11C5 11 1 7 1 2.2z"/></svg>07700 900123</li>
    <li><svg viewBox="0 0 12 12"><path d="M0 2h12v1.2L6 7 0 3.2zM0 4.6l6 3.8 6-3.8V10H0z"/></svg>info@brovencars.co.uk</li>
  </ul>
  <h4 class="cond" style="left:599px">Stay Connected</h4>
  <p class="news-note">Join our newsletter and find out more.</p>
  <div class="news-field">Email<svg viewBox="0 0 18 14"><path d="M0 0h18v2L9 8 0 2zM0 4l9 6 9-6v10H0z"/></svg></div>
  <h4 class="title cond" style="left:946px">Follow us on</h4>
  <div class="social"><span></span><span></span><span></span></div>
  <div class="rule"></div>
  <p class="copyright">Copyright © 2018 Broven Cars. All rights reserved.</p>
</footer>

</body>
</html>
```